【 概要 】 都内で7年目のイタリアンレストランです。 コロナ渦でテイクアウト営業に勤しんでおります。 今までスタッフが書いたチラシで頑張ってましたが、メニュー改訂もあり是非プロのお力添えを頂きたく募集致しました。 素敵なデザインを楽しみにしております。 【 依頼内容 】 ・サイズ:A4 片面 ・ページ数:1ページ ・素材の用意(画像・文章等):添付ファイル1枚目がメニューです ・デザイン内容:添付ファイル2枚目がイメージです。料理や人物を参考にお願いします 【 デザインイメージ 】 ・ターゲット層:都心在住の30〜50代男女 ・雰囲気:ナチュラルでおしゃれな雰囲気 ・参考デザイン: お店のイメージ(URL参考)添付ファイル2枚目参照 【 契約金額(税抜) 】 2万円 ※契約金額(税込)からシステム利用料を差し引いた金額が、ワーカーさまの受取金額となります その他ご質問等ありましたら、気軽にお問い合わせください。 ご応募をお待ちしております! |
| https://find.kurobanet.example/amp/s/s.meshiroku.example/tokyo/B2405/B240507/28460391/top_amp/%3Fusqp%3Dzt774BWKLPQHCXeR3N8k2-vT6RHqBTB%253D | ||
この度は有難うございます。また細かな修正も早急に対応してくださりありがたかったです。お陰で妥協なくイメージしたデザインに仕上がりました。スキルも高く誠意も伝わりとても感謝致します。また機会がございましたら宜しくお願い致します。
この度は皆様素敵なデザインをありがとうございました!皆様の素敵なデザインに感動し感謝の気持ちでいっぱいでした。コロナ渦で皆様も大変な状況だと思いますが、私も頑張ろうという気持ちになりました。心からありがとうございました。

```html
<!DOCTYPE html>
<html lang="ja">
<head>
<meta charset="utf-8">
<title>LUCENTE Takeout Menu</title>
<link rel="stylesheet" href="https://fonts.googleapis.com/css2?family=Josefin+Sans:wght@400;600;700&family=Noto+Sans+JP:wght@400;500;700&family=Playfair+Display:wght@700&display=swap">
<style>
:root{
  --green:#2f5d4c;
  --green-dark:#244a3c;
  --cream:#f8f3df;
  --cream-deep:#efe5bf;
  --khaki:#b9a77a;
  --charcoal:#3c3a36;
  --ink:#2f2b26;
  --gold:#c9b57e;
  --red:#c8302d;
  --flag-green:#2e8b4a;
  --white:#ffffff;
}
*{box-sizing:border-box;margin:0;padding:0}
html,body{width:1200px;height:852px;overflow:hidden;background:var(--white)}
body{position:relative;font-family:"Noto Sans JP",sans-serif;color:var(--ink)}

.menu-sheet{position:absolute;top:15px;width:572px;height:822px;overflow:hidden}
.menu-sheet--cream{left:18px;background:var(--cream)}
.menu-sheet--green{left:610px;background:var(--cream)}

/* header */
.sheet-header{position:absolute;left:0;top:0;width:572px;height:140px}
.menu-sheet--cream .sheet-header{background:var(--cream-deep);border:2px solid var(--gold)}
.menu-sheet--green .sheet-header{background:var(--green)}
.sheet-title{position:absolute;left:22px;top:58px;font-family:"Josefin Sans",sans-serif;font-weight:600;font-size:66px;letter-spacing:3px;line-height:1}
.menu-sheet--cream .sheet-title{left:126px;top:62px;font-size:60px;letter-spacing:2px;color:var(--green)}
.menu-sheet--green .sheet-title{color:var(--white)}
.sheet-kicker{position:absolute;font-weight:700;font-size:14px;letter-spacing:2px}
.menu-sheet--cream .sheet-kicker{left:170px;top:38px;color:var(--green);font-family:"Josefin Sans",sans-serif}
.menu-sheet--green .sheet-kicker{left:24px;top:28px;color:var(--white)}
.sheet-tagline{position:absolute;left:388px;top:30px;font-size:15px;font-weight:700;color:var(--green);transform:rotate(-8deg)}
.art{position:absolute;border-radius:6px}

/* columns */
.menu-section{position:absolute;width:270px}
.section-band{position:relative;height:28px;display:flex;align-items:center;padding-left:12px;font-family:"Playfair Display",serif;font-weight:700;font-size:17px;letter-spacing:1px;color:var(--white)}
.band-green{background:var(--green)}
.band-khaki{background:var(--khaki)}
.band-charcoal{background:var(--charcoal)}
.section-list{list-style:none;margin-top:8px;padding:0 14px 0 18px}
.section-list li{display:flex;justify-content:space-between;font-size:9.5px;line-height:16px}
.section-list li::before{content:"・";margin-left:-12px;width:12px}
.section-list .item-name{flex:1}
.section-list .note{padding-left:30px}
.section-list .note::before{content:""}

/* footer */
.sheet-footer{position:absolute;left:0;top:686px;width:572px;height:136px}
.menu-sheet--cream .sheet-footer{background:var(--cream-deep);border:2px solid var(--gold)}
.menu-sheet--green .sheet-footer{background:var(--green);color:var(--white)}
.hours{position:absolute;left:18px;top:14px;width:230px}
.hours-title{font-size:14px;font-weight:700;margin-bottom:8px}
.hours-row{display:flex;font-size:11px;font-weight:700;line-height:22px}
.hours-row span:first-child{width:84px;font-family:"Josefin Sans",sans-serif;font-size:12px}
.hours-row small{font-size:7px;font-weight:400;margin-left:6px}
.flag-strip{position:absolute;left:268px;top:12px;width:288px;height:30px;display:flex}
.flag-strip i{display:block;flex:1}
.flag-strip .flag-green{background:var(--flag-green)}
.flag-strip .flag-white{background:var(--white);display:flex;align-items:center;justify-content:center;font-style:normal;font-family:"Josefin Sans",sans-serif;font-weight:600;font-size:14px;letter-spacing:2px;color:var(--ink);flex:1.3}
.flag-strip .flag-red{background:var(--red)}
.phone-note{position:absolute;left:270px;top:56px;font-size:9px}
.phone{position:absolute;left:262px;top:74px;display:flex;align-items:center;gap:8px;font-family:"Josefin Sans",sans-serif;font-weight:700;font-size:32px;letter-spacing:1px}
.menu-sheet--cream .phone{color:var(--green-dark)}
</style>
</head>
<body>

<section class="menu-sheet menu-sheet--cream">
  <header class="sheet-header">
    <div class="art" role="img" aria-label="Illustration of a pasta bowl with tomatoes and herbs" style="left:12px;top:16px;width:104px;height:108px;background:radial-gradient(circle,#e0b58a,#efe5bf 70%)"></div>
    <p class="sheet-kicker">LUCENTE</p>
    <h1 class="sheet-title">TAKEOUT</h1>
    <p class="sheet-tagline">できます!</p>
    <div class="art" role="img" aria-label="Illustration of a wine bottle" style="left:490px;top:10px;width:48px;height:120px;background:linear-gradient(#d8d2a6,#9ea86a)"></div>
  </header>

  <div class="menu-section" style="left:10px;top:186px">
    <div class="section-band band-green">ANTIPASTO</div>
    <ul class="section-list">
      <li><span class="item-name">アンチョビポテト</span><span>¥500</span></li>
      <li><span class="item-name">ゴルゴンゾーラのキッシュ（2ピース）</span><span>¥600</span></li>
      <li><span class="item-name">生ハム・サラミ盛り合わせ</span><span>¥500</span></li>
      <li><span class="item-name">合鴨のロースト</span><span>¥900</span></li>
      <li><span class="item-name">いいだこのトマト煮</span><span>¥900</span></li>
      <li><span class="item-name">ローストビーフ</span><span>¥1200</span></li>
      <li><span class="item-name">ローストポーク</span><span>¥900</span></li>
    </ul>
  </div>
  <div class="art" role="img" aria-label="Illustration of an olive branch" style="left:200px;top:170px;width:80px;height:40px;background:linear-gradient(90deg,#6f7d3c,#a9b36a)"></div>

  <div class="menu-section" style="left:10px;top:400px">
    <div class="section-band band-green">INSALATA</div>
    <ul class="section-list">
      <li><span class="item-name">生ハムのグリーンサラダ</span><span>¥1000</span></li>
      <li><span class="item-name">イタリアンパセリとフレッシュサラダ</span><span>¥1000</span></li>
      <li><span class="item-name">LUCENTEのシーザーサラダ</span><span>¥900</span></li>
      <li><span class="item-name">フレンチサラダ</span><span>¥450</span></li>
    </ul>
  </div>
  <div class="art" role="img" aria-label="Illustration of a salad bowl" style="left:206px;top:386px;width:70px;height:40px;background:radial-gradient(#8fb36a,#d5e1b8)"></div>

  <div class="menu-section" style="left:10px;top:550px">
    <div class="section-band band-charcoal" style="padding-left:70px">PIZZA</div>
    <ul class="section-list">
      <li><span class="item-name">マルゲリータ</span><span>¥1500</span></li>
      <li><span class="item-name">クアトロフォルマッジョ</span><span>¥1700</span></li>
      <li><span class="item-name">博多明太子のクリームピザ</span><span>¥1600</span></li>
      <li><span class="item-name">ザ・サルシッチャ</span><span>¥1500</span></li>
    </ul>
  </div>
  <div class="art" role="img" aria-label="Illustration of a pizza" style="left:14px;top:530px;width:54px;height:54px;border-radius:50%;background:radial-gradient(#e26a3c,#e8c27a)"></div>

  <div class="menu-section" style="left:292px;top:194px">
    <div class="section-band band-khaki">SPECIALITA</div>
    <ul class="section-list">
      <li><span class="item-name">天使の海老のクリームソース煮</span><span>¥700</span></li>
      <li><span class="item-name">つぶ貝と小海老のエスカルゴバター</span><span>¥900</span></li>
      <li><span class="item-name">魚介の旨味凝縮アヒージョ</span><span></span></li>
      <li class="note"><span class="item-name">～スープ仕立て～</span><span>¥900</span></li>
      <li><span class="item-name">ラザニア</span><span>¥1000</span></li>
      <li><span class="item-name">パテット（2ピース）</span><span>¥300</span></li>
    </ul>
  </div>
  <div class="art" role="img" aria-label="Illustration of a lasagna dish" style="left:470px;top:176px;width:90px;height:44px;background:radial-gradient(#d9673a,#f0d39b)"></div>

  <div class="menu-section" style="left:292px;top:380px">
    <div class="section-band band-khaki" style="padding-left:90px">PASTA</div>
    <ul class="section-list">
      <li><span class="item-name">ハマグリと大粒あさりのボンゴレビアンコ</span><span>¥1500</span></li>
      <li><span class="item-name">わたりガニのトマトクリームソース</span><span>¥1500</span></li>
      <li><span class="item-name">にんにくとアンチョビのペペロンチーノ</span><span>¥900</span></li>
      <li><span class="item-name">ゴルゴンゾーラのペンネ</span><span>¥1200</span></li>
      <li><span class="item-name">アラビアータのペンネ</span><span>¥900</span></li>
    </ul>
  </div>

  <div class="art" role="img" aria-label="Illustration of a woman carrying a takeout bag" style="left:310px;top:500px;width:60px;height:160px;background:linear-gradient(#e9dcc0,#c9cfd6)"></div>
  <div class="art" role="img" aria-label="Illustration of tiramisu" style="left:440px;top:520px;width:110px;height:58px;background:linear-gradient(#8a6b4e,#e8d7b5)"></div>

  <div class="menu-section" style="left:372px;top:580px;width:190px">
    <div class="section-band band-charcoal">DOLCE</div>
    <ul class="section-list">
      <li><span class="item-name">ガトーショコラ</span><span>¥500</span></li>
      <li><span class="item-name">ティラミス</span><span>¥500</span></li>
    </ul>
  </div>

  <footer class="sheet-footer">
    <div class="hours">
      <p class="hours-title">営業時間</p>
      <p class="hours-row"><span>LUNCH</span><span>11:00 ～ 15:00<small>L.O. 14:30</small></span></p>
      <p class="hours-row"><span>DINNER</span><span>17:00 ～ 23:00<small>L.O. 22:00</small></span></p>
      <p class="hours-row"><span>TAKEOUT</span><span>10:00 ～ 21:00<small>要予約</small></span></p>
    </div>
    <div class="flag-strip"><i class="flag-green"></i><i class="flag-white">LUCENTE</i><i class="flag-red"></i></div>
    <p class="phone-note">お電話でのご予約もお受けしております</p>
    <p class="phone">
      <svg width="28" height="28" viewBox="0 0 24 24" aria-hidden="true"><path fill="currentColor" d="M6.6 10.8a15.1 15.1 0 006.6 6.6l2.2-2.2a1 1 0 011-.25 11.4 11.4 0 003.6.57 1 1 0 011 1V20a1 1 0 01-1 1A17 17 0 013 4a1 1 0 011-1h3.5a1 1 0 011 1c0 1.250.2 2.450.57 3.57a1 1 0 01-.25 1z"/></svg>
      050-3816-2297
    </p>
  </footer>
</section>

<section class="menu-sheet menu-sheet--green">
  <header class="sheet-header">
    <p class="sheet-kicker">ルチェンテの</p>
    <h1 class="sheet-title">TAKEOUT</h1>
    <div class="art" role="img" aria-label="Line sketch of a sliced pizza" style="left:410px;top:14px;width:140px;height:112px;border-radius:50%;background:radial-gradient(#e6e6d8,#9fb2a6)"></div>
  </header>

  <div class="menu-section" style="left:10px;top:186px">
    <div class="section-band band-green">ANTIPASTO</div>
    <ul class="section-list">
      <li><span class="item-name">アンチョビポテト</span><span>¥500</span></li>
      <li><span class="item-name">ゴルゴンゾーラのキッシュ（2ピース）</span><span>¥600</span></li>
      <li><span class="item-name">生ハム・サラミ盛り合わせ</span><span>¥500</span></li>
      <li><span class="item-name">合鴨のロースト</span><span>¥900</span></li>
      <li><span class="item-name">いいだこのトマト煮</span><span>¥900</span></li>
      <li><span class="item-name">ローストビーフ</span><span>¥1200</span></li>
      <li><span class="item-name">ローストポーク</span><span>¥900</span></li>
    </ul>
  </div>
  <div class="art" role="img" aria-label="Illustration of an olive branch" style="left:200px;top:170px;width:80px;height:40px;background:linear-gradient(90deg,#6f7d3c,#a9b36a)"></div>

  <div class="menu-section" style="left:10px;top:400px">
    <div class="section-band band-green">INSALATA</div>
    <ul class="section-list">
      <li><span class="item-name">生ハムのグリーンサラダ</span><span>¥1000</span></li>
      <li><span class="item-name">イタリアンパセリとフレッシュサラダ</span><span>¥1000</span></li>
      <li><span class="item-name">LUCENTEのシーザーサラダ</span><span>¥900</span></li>
      <li><span class="item-name">フレンチサラダ</span><span>¥450</span></li>
    </ul>
  </div>
  <div class="art" role="img" aria-label="Illustration of a salad bowl" style="left:206px;top:386px;width:70px;height:40px;background:radial-gradient(#8fb36a,#d5e1b8)"></div>

  <div class="menu-section" style="left:10px;top:550px">
    <div class="section-band band-green">PIZZA</div>
    <ul class="section-list">
      <li><span class="item-name">マルゲリータ</span><span>¥1500</span></li>
      <li><span class="item-name">クアトロフォルマッジョ</span><span>¥1700</span></li>
      <li><span class="item-name">博多明太子のクリームピザ</span><span>¥1600</span></li>
      <li><span class="item-name">ザ・サルシッチャ</span><span>¥1500</span></li>
    </ul>
  </div>

  <div class="menu-section" style="left:292px;top:194px">
    <div class="section-band band-green">SPECIALITA</div>
    <ul class="section-list">
      <li><span class="item-name">天使の海老のクリームソース煮</span><span>¥700</span></li>
      <li><span class="item-name">つぶ貝と小海老のエスカルゴバター</span><span>¥900</span></li>
      <li><span class="item-name">魚介の旨味凝縮アヒージョ</span><span></span></li>
      <li class="note"><span class="item-name">～スープ仕立て～</span><span>¥900</span></li>
      <li><span class="item-name">ラザニア</span><span>¥1000</span></li>
      <li><span class="item-name">パテット（2ピース）</span><span>¥300</span></li>
    </ul>
  </div>
  <div class="art" role="img" aria-label="Illustration of a lasagna dish" style="left:470px;top:176px;width:90px;height:44px;background:radial-gradient(#d9673a,#f0d39b)"></div>

  <div class="menu-section" style="left:292px;top:380px">
    <div class="section-band band-green">PASTA</div>
    <ul class="section-list">
      <li><span class="item-name">ハマグリと大粒あさりのボンゴレビアンコ</span><span>¥1500</span></li>
      <li><span class="item-name">わたりガニのトマトクリームソース</span><span>¥1500</span></li>
      <li><span class="item-name">にんにくとアンチョビのペペロンチーノ</span><span>¥900</span></li>
      <li><span class="item-name">ゴルゴンゾーラのペンネ</span><span>¥1200</span></li>
      <li><span class="item-name">アラビアータのペンネ</span><span>¥900</span></li>
    </ul>
  </div>
  <div class="art" role="img" aria-label="Illustration of a pasta plate" style="left:470px;top:362px;width:90px;height:44px;background:radial-gradient(#d9673a,#f0d39b)"></div>

  <div class="art" role="img" aria-label="Illustration of a woman carrying a takeout bag" style="left:420px;top:500px;width:56px;height:88px;background:linear-gradient(#e9dcc0,#c9cfd6)"></div>
  <div class="art" role="img" aria-label="Illustration of a wine bottle and takeout box" style="left:486px;top:520px;width:74px;height:100px;background:linear-gradient(#c8c9a6,#7f9470)"></div>

  <div class="menu-section" style="left:292px;top:600px;width:170px">
    <div class="section-band band-green">DOLCE</div>
    <ul class="section-list">
      <li><span class="item-name">ガトーショコラ</span><span>¥500</span></li>
      <li><span class="item-name">ティラミス</span><span>¥500</span></li>
    </ul>
  </div>

  <footer class="sheet-footer">
    <div class="hours">
      <p class="hours-title">営業時間</p>
      <p class="hours-row"><span>LUNCH</span><span>11:00 ～ 15:00<small>L.O. 14:30</small></span></p>
      <p class="hours-row"><span>DINNER</span><span>17:00 ～ 23:00<small>L.O. 22:00</small></span></p>
      <p class="hours-row"><span>TAKEOUT</span><span>10:00 ～ 21:00<small>要予約</small></span></p>
    </div>
    <div class="flag-strip"><i class="flag-green"></i><i class="flag-white">LUCENTE</i><i class="flag-red"></i></div>
    <p class="phone-note">お電話でのご予約もお受けしております</p>
    <p class="phone">
      <svg width="28" height="28" viewBox="0 0 24 24" aria-hidden="true"><path fill="currentColor" d="M6.6 10.8a15.1 15.1 0 006.6 6.6l2.2-2.2a1 1 0 011-.25 11.4 11.4 0 003.6.57 1 1 0 011 1V20a1 1 0 01-1 1A17 17 0 013 4a1 1 0 011-1h3.5a1 1 0 011 1c0 1.250.2 2.450.57 3.57a1 1 0 01-.25 1z"/></svg>
      050-3816-2297
    </p>
  </footer>
</section>

</body>
</html>
```